Harbor Key Realty - New Agent Opportunity Overview

We want to create a one (1) page brochure to highlight what Harbor Key Realty (a real estate brokerage) offers new agents. I have uploaded a Word doc that has all the text we want on the flyer. We want a professional looking design.
Industry/Entity Type
Real Estate Agent
Colors
3176b5
33a6d7

```html
<!DOCTYPE html>
<html lang="en">
<head>
<meta charset="utf-8">
<title>Harbor Key Realty – New Agent Opportunity</title>
<link rel="stylesheet" href="https://fonts.googleapis.com/css2?family=Jost:wght@400;500;600;700&display=swap">
<style>
  :root{
    --brand-blue:#3176b5;
    --sky-blue:#33a6d7;
    --deep-blue:#2a5f9e;
    --pale:#e6ecf6;
    --orange:#f7931e;
    --ink:#111418;
    --white:#ffffff;
    --page:#eef1f5;
  }
  *{box-sizing:border-box;margin:0;padding:0}
  html,body{width:1200px;height:1036px;overflow:hidden}
  body{background:var(--page);font-family:"Jost",sans-serif;position:relative}
  .flyer{position:absolute;left:200px;top:0;width:800px;height:1036px;background:var(--brand-blue);overflow:hidden;color:var(--white)}
  .flyer-bg{position:absolute;inset:0}
  .brand{position:absolute;left:210px;top:62px;width:560px;text-align:center;color:var(--ink);font-weight:600;font-size:46px;letter-spacing:4px;text-transform:uppercase;line-height:1}
  .headline{position:absolute;left:40px;top:208px;width:730px;font-size:26px;font-weight:500;color:var(--white);padding-bottom:6px;border-bottom:3px solid var(--white);white-space:nowrap}
  .section-title{color:var(--ink);font-weight:700;font-size:19px;letter-spacing:.5px;text-transform:uppercase;margin-bottom:6px;white-space:nowrap}
  .feature-list{list-style:none}
  .feature-list li{font-size:16px;line-height:1.32;padding-left:20px;position:relative}
  .feature-list li::before{content:"";position:absolute;left:2px;top:6px;width:10px;height:10px;background:var(--white);clip-path:polygon(50% 0,100% 45%,85% 45%,85% 100%,15% 100%,15% 45%,0 45%)}
  .col-left{position:absolute;left:40px;top:300px;width:400px}
  .col-left .section{margin-bottom:30px}
  .col-right{position:absolute;left:450px;top:300px;width:325px}
  .col-right .feature-list li{font-size:15px}
  .split-table{margin-top:16px;width:100%;border-collapse:collapse;font-size:14px}
  .split-table th{font-weight:600;color:var(--ink);text-align:left;padding:6px 8px;background:var(--white);white-space:nowrap}
  .split-table th.split{text-align:center}
  .split-table td{padding:5px 8px;border:1.5px solid var(--white);white-space:nowrap}
  .split-table td.split{text-align:center;width:32%}
  .photo-house{position:absolute;left:485px;top:575px;width:295px;height:315px;border-radius:46% 40% 30% 30%;background:radial-gradient(ellipse at 50% 35%,#f3d3b4 0%,#d9825a 35%,#5d9e3a 70%,#3f7d2a 100%)}
  .cta{position:absolute;left:330px;top:905px;width:470px;height:131px;background:var(--orange);border-radius:34px 0 0 0;color:var(--white);font-weight:600;font-size:22px;line-height:1.3;text-transform:uppercase;padding:30px 0 0 28px;white-space:nowrap}
  .cta span{display:block}
  .cta span+span{padding-left:30px}
</style>
</head>
<body>
<main class="flyer">
  <svg class="flyer-bg" width="800" height="1036" viewBox="0 0 800 1036" aria-hidden="true">
    <rect x="0" y="0" width="75" height="190" fill="var(--sky-blue)"/>
    <rect x="75" y="0" width="85" height="190" fill="var(--deep-blue)"/>
    <rect x="160" y="0" width="640" height="170" fill="var(--sky-blue)"/>
    <rect x="160" y="170" width="640" height="3" fill="var(--deep-blue)"/>
    <path d="M0 940 C 160 800, 330 760, 520 790 C 640 810, 720 770, 800 700 L800 1036 L0 1036 Z" fill="var(--pale)"/>
    <path d="M0 975 C 170 840, 330 810, 520 840 C 640 860, 720 830, 800 770 L800 1036 L0 1036 Z" fill="var(--sky-blue)"/>
    <path d="M0 1036 L0 1015 C 170 900, 330 870, 520 890 C 620 900, 700 890, 800 860 L800 1036 Z" fill="var(--brand-blue)"/>
  </svg>

  <div class="brand">Harbor Key Realty</div>

  <h1 class="headline">HKR Home Center Brookhaven Falls, Maryland is Now Open!</h1>

  <div class="col-left">
    <section class="section">
      <h2 class="section-title">Consumer Direct Advantage</h2>
      <ul class="feature-list">
        <li>Lender Referrals</li>
        <li>Nestfind Leads</li>
        <li>Shared Lender Leads</li>
        <li>Homelist.net / HouseHuntLocal.com</li>
        <li>Credit Trigger Campaigns</li>
        <li>Consumer Behavior Campaigns</li>
        <li>HKR Call Center Marketing Team</li>
        <li>HKR Sponsored Local Events</li>
      </ul>
    </section>
    <section class="section">
      <h2 class="section-title">Complete Support System</h2>
      <ul class="feature-list">
        <li>Powerful Suite of Cloud Based Tools</li>
        <li>IDX, CRM and Transaction Management</li>
        <li>HKR Call Center Support for Leads and Deals</li>
        <li>Transaction Coordinator</li>
        <li>Virtual Assistants Available</li>
        <li>24/7 Workspace Access</li>
        <li>Coaching / Mentoring</li>
        <li>Social Media / Marketing Expertise</li>
        <li>Nationwide Partnerships with Top Lenders</li>
      </ul>
    </section>
  </div>

  <div class="col-right">
    <h2 class="section-title">Maximized Compensation</h2>
    <ul class="feature-list">
      <li>No desk fees. No royalty fees. No franchise fees.</li>
      <li>Company paid E&amp;O</li>
      <li>Transaction fee of $550 includes Transaction Coordinator</li>
    </ul>
    <table class="split-table">
      <thead>
        <tr><th>Type of Deal</th><th class="split">Commission Split</th></tr>
      </thead>
      <tbody>
        <tr><td>Self-Generated</td><td class="split">90% / 10%</td></tr>
        <tr><td>Lender Referred Leads</td><td class="split">70% / 30%</td></tr>
        <tr><td>HKR Generated Leads / Referrals</td><td class="split">55% / 45%</td></tr>
      </tbody>
    </table>
  </div>

  <div class="photo-house" role="img" aria-label="Photo of a two-storey suburban house with a terracotta roof on a green lawn with shrubs"></div>

  <div class="cta">
    <span>Ignite your real estate business</span>
    <span>Join Harbor Key Realty</span>
  </div>
</main>
</body>
</html>
```